依頼詳細
タイトル+20~30行のテキストが主。
テキストをお読みいただき雰囲気に合ったデザインをお願いします。
イメージ
重厚感、誠実、まじめ。
もし動画にするならBGMはカゼノワの「白い石の坂道」のイメージ。
曇り空に一筋の光
とか
全面的に黒い雰囲気の中に一滴の赤

或いは画像の中の青空を活かしても面白いかもしれません。
記載項目
・添付のテキスト
・背景に使う写真は添付ファイルを使ってもいいし、使わなくても構いません
・最後の「灯野空建株式会社」は検索ウィンドウとし、右側に「検索」ボタンをつけてください。
・チラシ最下段に「説明会情報は弊社HPでご確認ください」
サイズ
A4
ページ数
片面
希望イメージ
シンプル 複雑
単色 カラフル
暗い 明るい
日常 高級
遊び心 厳粛
未来的 伝統的
女性的 男性的
希望する色
水色系、グレー系
納品ファイル
• フォトショップ形式 (.psd)
補足説明
追加でお願いするポスターは約72cm×22cmで一般的なサイズ
合同企業説明会のときにブースを通る学生さんの足を止めるためのインパクト大なポスターを希望します。

希望通りのイメージで仕上げて頂きました。
ありがとうございます。

多数のご提案頂きありがとうございました。

```html
<!DOCTYPE html>
<html lang="ja">
<head>
<meta charset="utf-8">
<title>スーツを着た仕事が幸せだと思い込んでないか？</title>
<link rel="stylesheet" href="https://fonts.googleapis.com/css2?family=Noto+Sans+JP:wght@400;500;700;900&display=swap">
<style>
  :root {
    --sky-deep: #0b1a33;
    --sky-mid: #1f3f6e;
    --sky-light: #6f93bf;
    --sun: #fff7e6;
    --text: #ffffff;
    --text-soft: #e6edf6;
    --field-bg: #ffffff;
    --field-text: #222222;
    --button-bg: #d8dde3;
    --button-line: #9aa3ad;
  }
  * { margin: 0; padding: 0; box-sizing: border-box; }
  html, body { width: 846px; height: 1200px; overflow: hidden; background: var(--sky-deep); }
  .poster {
    position: relative;
    width: 846px;
    height: 1200px;
    overflow: hidden;
    font-family: "Noto Sans JP", sans-serif;
    color: var(--text);
  }
  .sky-photo {
    position: absolute;
    inset: 0;
    background:
      radial-gradient(circle at 300px 580px, var(--sun) 0, rgba(255,247,230,0.85) 40px, rgba(200,220,245,0.45) 120px, rgba(111,147,191,0) 300px),
      radial-gradient(ellipse at 45% 45%, var(--sky-light) 0%, var(--sky-mid) 45%, var(--sky-deep) 85%);
  }
  .headline {
    position: absolute;
    writing-mode: vertical-rl;
    font-size: 116px;
    font-weight: 900;
    line-height: 1;
    white-space: nowrap;
    color: var(--text);
  }
  .headline--first  { left: 724px; top: 22px;  letter-spacing: -18px; }
  .headline--second { left: 604px; top: 128px; letter-spacing: -14px; }
  .headline--third  { left: 484px; top: 296px; letter-spacing: -23px; }

  .message {
    position: absolute;
    left: 34px;
    top: 30px;
    width: 360px;
    font-size: 14px;
    font-weight: 500;
    line-height: 35px;
    color: var(--text-soft);
  }
  .message p + p { margin-top: 35px; }

  .company-search {
    position: absolute;
    left: 205px;
    top: 1050px;
    width: 240px;
  }
  .company-search__lead {
    font-size: 11px;
    font-weight: 500;
    letter-spacing: 0.05em;
    margin-bottom: 5px;
  }
  .company-search__bar {
    display: flex;
    height: 28px;
    border: 1px solid var(--button-line);
    background: var(--field-bg);
  }
  .company-search__field {
    flex: 1;
    padding: 0 8px;
    font-size: 13px;
    font-weight: 700;
    line-height: 26px;
    color: var(--field-text);
  }
  .company-search__button {
    width: 46px;
    border-left: 1px solid var(--button-line);
    background: var(--button-bg);
    font-size: 11px;
    line-height: 26px;
    text-align: center;
    color: var(--field-text);
  }
  .company-search__note {
    margin-top: 5px;
    font-size: 9px;
    color: var(--text-soft);
  }
</style>
</head>
<body>
<main class="poster">
  <div class="sky-photo" role="img" aria-label="曇り空と電柱のシルエット、雲間から差し込む一筋の太陽の光の写真"></div>

  <section class="message">
    <p>人生にレールなんて無い。<br>あるのは自分と世界との関わりだけだ。<br>幸せを規定するのは世界じゃない。<br>自分自身だ。<br>全ての価値観を捨てたとき、<br>未来に何を掴むんだろう。</p>
    <p>やりたいことが見つからないなんて当たり前だ。<br>試しに隣の大人に聞いてみたらいい。<br>「やりたいこと、仕事にできてますか？」<br>きっと曖昧な答えしか返ってこない。</p>
    <p>もう認めよう。<br>君は特別じゃない。<br>何者にもなれはしない。<br>逃避する弱さ、<br>自分探しなんてもう十分だ。</p>
    <p>認めよう。<br>全てそこから始まる。</p>
    <p>誰もかれも目的地なんてわかってない。<br>それでも、<br>それでも歩きだしたい。</p>
    <p>変わり続ける自分は<br>会社に何を期待すればいいんだろう。</p>
  </section>

  <h1 class="headline-group">
    <span class="headline headline--first">スーツを着た仕事が</span>
    <span class="headline headline--second">幸せだと</span>
    <span class="headline headline--third">思い込んでないか？</span>
  </h1>

  <footer class="company-search">
    <p class="company-search__lead">企業活動のその先を見据える――</p>
    <div class="company-search__bar">
      <span class="company-search__field">灯野空建株式会社</span>
      <span class="company-search__button">検索</span>
    </div>
    <p class="company-search__note">説明会情報は弊社HPでご確認ください</p>
  </footer>
</main>
</body>
</html>
```